Professional, modern and unique business card. We are looking to present a new look to our business cards however we don't want to divert too far away from original template. We want social media links and our 3 office addresses on the backside of the business cards. Please see attached business card templates for ideas.
Lakeshore Realty Color Code:
R: 7
G:63
B:86

Target Market(s)

Real Estate

Industry/Entity Type

Real Estate

Contact Information for Business Card

Follow the attached templates. In need of a more modern and unique touch but don't want to divert from the original theme or color.
Lakeshore Realty Color Code:
R: 7
G:63
B:86

Font styles to use
Serif

Requirements
Must have
• Lakeshore Realty logo, Lakeshore realty colors, social media links, 3 office addresses,
Nice to have
• information about Lakeshore Realty and QR codes. You can check out www.mylakeshorehomes.example

```html
<!DOCTYPE html>
<html lang="en">
<head>
<meta charset="utf-8">
<title>Lakeshore Realty Business Card</title>
<link href="https://fonts.googleapis.com/css2?family=Lora:wght@400;500;600&display=swap" rel="stylesheet">
<style>
  :root {
    --backdrop: #b9babb;
    --brand: #073f56;
    --card-white: #ffffff;
    --ink: #1b1b1b;
    --on-brand: #ffffff;
    --rule-on-brand: rgba(255,255,255,0.8);
  }
  html, body {
    margin: 0;
    padding: 0;
    width: 1200px;
    height: 930px;
    overflow: hidden;
    background: var(--backdrop);
    font-family: "Lora", serif;
  }
  .canvas {
    position: relative;
    width: 1200px;
    height: 930px;
  }
  .card {
    position: absolute;
    width: 560px;
    height: 320px;
    border-radius: 26px;
    box-shadow: 0 10px 24px rgba(0,0,0,0.22);
    box-sizing: border-box;
  }
  .brand {
    display: flex;
    align-items: center;
    gap: 12px;
    font-weight: 600;
    letter-spacing: 0.06em;
    text-transform: uppercase;
    white-space: nowrap;
  }
  .brand__dot {
    width: 20px;
    height: 20px;
    border-radius: 50%;
    background: currentColor;
    flex: none;
  }

  /* Back side */
  .card--back {
    left: 70px;
    top: 110px;
    background: var(--brand);
    color: var(--on-brand);
  }
  .card--back .brand {
    position: absolute;
    left: 0;
    right: 0;
    top: 84px;
    justify-content: center;
    font-size: 32px;
  }
  .socials {
    position: absolute;
    left: 0;
    right: 0;
    top: 148px;
    margin: 0;
    padding: 0;
    list-style: none;
    display: flex;
    justify-content: center;
    gap: 26px;
    font-size: 13px;
  }
  .socials li {
    display: flex;
    align-items: center;
    gap: 7px;
  }
  .socials__mark {
    width: 9px;
    height: 9px;
    border: 1.5px solid var(--on-brand);
    border-radius: 50%;
  }
  .offices {
    position: absolute;
    left: 28px;
    right: 28px;
    bottom: 34px;
    display: flex;
    font-size: 12.5px;
    line-height: 1.5;
  }
  .office {
    flex: 1;
    padding: 0 12px;
    font-style: normal;
  }
  .office + .office {
    border-left: 1.5px solid var(--rule-on-brand);
  }

  /* Front side */
  .card--front {
    left: 570px;
    top: 500px;
    background: var(--card-white);
    color: var(--ink);
  }
  .card--front .brand {
    position: absolute;
    left: 34px;
    top: 96px;
    font-size: 24px;
    color: var(--ink);
  }
  .person {
    position: absolute;
    right: 34px;
    top: 34px;
    text-align: right;
  }
  .person__name {
    margin: 0;
    font-size: 22px;
    font-weight: 600;
    color: var(--brand);
    text-transform: uppercase;
    letter-spacing: 0.03em;
  }
  .person__title {
    margin: 2px 0 0;
    font-size: 13px;
  }
  .divider {
    position: absolute;
    left: 34px;
    right: 34px;
    top: 160px;
    height: 1.5px;
    background: var(--brand);
  }
  .contacts {
    position: absolute;
    left: 34px;
    top: 182px;
    margin: 0;
    padding: 0;
    list-style: none;
    font-size: 15px;
    line-height: 1.6;
  }
  .contacts li {
    display: flex;
    align-items: center;
    gap: 10px;
  }
  .contacts svg {
    width: 12px;
    height: 12px;
    fill: none;
    stroke: var(--brand);
    stroke-width: 1.6;
    flex: none;
  }
</style>
</head>
<body>
<main class="canvas">
  <section class="card card--back" aria-label="Card back">
    <div class="brand"><span class="brand__dot"></span>Lakeshore Realty</div>
    <ul class="socials" aria-label="Social media">
      <li><span class="socials__mark"></span>@lakeshorerealty</li>
      <li><span class="socials__mark"></span>/lakeshorerealty</li>
      <li><span class="socials__mark"></span>@lakeshorehomes</li>
    </ul>
    <div class="offices">
      <address class="office">412 Harbor Blvd<br>Maple Point, NY 10950</address>
      <address class="office">78-20 Willow Ave<br>Cedar Bay, NY 10951</address>
      <address class="office">905 Lantern St<br>Oak Harbor, NY 10952</address>
    </div>
  </section>

  <section class="card card--front" aria-label="Card front">
    <div class="person">
      <p class="person__name">Daniel Reyes</p>
      <p class="person__title">Associate Real Estate Broker</p>
    </div>
    <div class="brand"><span class="brand__dot"></span>Lakeshore Realty</div>
    <div class="divider"></div>
    <ul class="contacts">
      <li><svg viewBox="0 0 12 12"><path d="M2 1.5l2 0 1 3-1.5 1a6 6 0 0 0 3 3l1-1.5 3 1 0 2a1 1 0 0 1-1 1A9 9 0 0 1 1 2.5a1 1 0 0 1 1-1z"/></svg>555-014-2873</li>
      <li><svg viewBox="0 0 12 12"><rect x="3" y="1" width="6" height="10" rx="1"/></svg>555-019-4410</li>
      <li><svg viewBox="0 0 12 12"><rect x="1" y="2.5" width="10" height="7"/><path d="M1 2.5l5 4 5-4"/></svg>info@mylakeshorehomes.example</li>
      <li><svg viewBox="0 0 12 12"><circle cx="6" cy="6" r="5"/><path d="M1 6h10M6 1c-3 3-3 7 0 10M6 1c3 3 3 7 0 10"/></svg>www.mylakeshorehomes.example</li>
    </ul>
  </section>
</main>
</body>
</html>
```